Healthcare website - Diabetic Shoes - Vitacor - No Cost

I am looking to upgrade my website. I do not want to use Wordpress, Adobe Muse or another designing program. The code should be easily editable using textpad or VI. After the project is done I want to easily add my custom PHP code.

Features
Creative and Modern Design .
Fully responsive site for use on mobile devices
bootstrap, jquery

My current website is
www.stridewellfeet.com

Target Market(s)

Older people who have diabetes. Target market is +60 years old, but we do have younger people going to the site to help out their parents.

Industry/Entity Type

Healthcare

Coding

Coded - Design and coding required

Number of Pages Required

2 page

Colors

Designer to choose colors to be used in the design.

Requirements
Must have
• The code should be easily editable using textpad or VI. After the project is done I want to easily add my custom PHP code.
• The first page will be the home page and the other page I need is this form.
• https://www.stridewellfeet.com/stride-well-feet-do-i-qualify.php
Should not have
• I do not want to use Wordpress, Adobe Muse or another designing program.

```html
<!DOCTYPE html>
<html lang="en">
<head>
<meta charset="utf-8">
<title>Stride Well Feet – Diabetic Shoes Covered by Vitacor</title>
<link href="https://fonts.googleapis.com/css2?family=Roboto+Condensed:wght@300;400;700&family=Open+Sans:wght@400;600&display=swap" rel="stylesheet">
<style>
:root{
  --blue:#4a7fad;
  --blue-dark:#3b6f9f;
  --title-blue:#3a74aa;
  --green:#6cc04a;
  --grey-panel:#efefef;
  --tile-light:#f1f1f1;
  --text:#333;
  --white:#fff;
}
*{box-sizing:border-box;margin:0;padding:0}
html,body{width:1200px;height:3203px;overflow:hidden}
body{position:relative;background:var(--white);font-family:"Open Sans",Arial,sans-serif;color:var(--text)}
.abs{position:absolute}

/* nav */
.topnav{left:0;top:0;width:1200px;height:60px;background:var(--blue)}
.topnav a{position:absolute;top:24px;color:var(--white);font:400 12px "Roboto Condensed",sans-serif;text-transform:uppercase;text-decoration:none;letter-spacing:.3px}
.brand-plate{left:470px;top:0;width:260px;height:128px}
.brand-name{left:470px;top:16px;width:260px;text-align:center;font:700 28px "Roboto Condensed",sans-serif;color:var(--blue-dark);letter-spacing:.5px}

/* hero */
.hero{left:0;top:60px;width:1200px;height:538px;
  background:
    radial-gradient(ellipse 170px 300px at 470px 280px,rgba(38,40,48,.95) 0%,rgba(38,40,48,.6) 55%,rgba(38,40,48,0) 100%),
    radial-gradient(ellipse 170px 300px at 730px 280px,rgba(38,40,48,.95) 0%,rgba(38,40,48,.6) 55%,rgba(38,40,48,0) 100%),
    radial-gradient(ellipse 90px 60px at 470px 70px,rgba(96,54,34,.95),rgba(96,54,34,0)),
    radial-gradient(ellipse 90px 60px at 730px 70px,rgba(96,54,34,.95),rgba(96,54,34,0)),
    repeating-linear-gradient(160deg,#7a4a3a 0 60px,#6b3f31 60px 64px,#835243 64px 130px,#6a3e30 130px 134px);}
.hero-shade{left:0;top:60px;width:1200px;height:538px;background:linear-gradient(180deg,rgba(0,0,0,.05),rgba(0,0,0,.25))}
.hero-kicker{left:0;top:240px;width:1200px;text-align:center;font:300 34px "Roboto Condensed",sans-serif;color:var(--white);text-transform:uppercase}
.hero-title{left:0;top:270px;width:1200px;text-align:center;font:700 68px "Roboto Condensed",sans-serif;color:var(--green);text-transform:uppercase;letter-spacing:-.5px}
.hero-sub{left:230px;top:356px;width:740px;text-align:center;font:400 11.5px/17px "Open Sans",sans-serif;color:var(--white)}
.hero-btn{left:520px;top:424px;width:160px;height:42px;border-radius:21px;background:var(--blue);border:2px solid #8fb3d3;color:var(--white);font:400 13px "Roboto Condensed",sans-serif;display:flex;align-items:center;justify-content:center;gap:8px}
.hero-arrow{top:310px;width:40px;height:40px;border-radius:50%;background:rgba(255,255,255,.35);display:flex;align-items:center;justify-content:center}

/* steps */
.steps-band{left:0;top:598px;width:1200px;height:239px;background:var(--blue)}
.steps-kicker{left:0;top:650px;width:1200px;text-align:center;font:300 28px "Roboto Condensed",sans-serif;color:var(--white);text-transform:uppercase}
.steps-title{left:0;top:680px;width:1200px;text-align:center;font:700 34px "Roboto Condensed",sans-serif;color:var(--white);text-transform:uppercase}
.step-card{top:756px;width:214px;height:166px;background:var(--grey-panel);border:2px solid var(--blue);display:flex;flex-direction:column;align-items:center;padding:28px 14px 0;text-align:center;font:400 13px/18px "Open Sans",sans-serif;color:#222}
.step-card svg{margin-bottom:14px}

/* diabetes */
.q-title{left:260px;top:962px;width:680px;height:66px;display:flex;align-items:center;justify-content:center;font:700 31px "Roboto Condensed",sans-serif;color:var(--title-blue);text-transform:uppercase}
.q-title .light{font-weight:300;color:#555;border:2px solid #a9d99a;padding:6px 10px;margin-left:6px}
.q-copy{left:230px;top:1040px;width:740px;text-align:center;font:400 11px/17px "Open Sans",sans-serif;color:#333}
.phone-pill{left:487px;top:1110px;width:224px;height:44px;border:2px solid var(--blue);border-radius:22px;display:flex;align-items:center;justify-content:center;font:700 25px "Roboto Condensed",sans-serif;color:var(--title-blue)}

/* products */
.products-band{left:0;top:1187px;width:1200px;height:90px;background:var(--green);text-align:center;color:var(--white);text-transform:uppercase}
.products-band .k{display:block;margin-top:16px;font:300 24px "Roboto Condensed",sans-serif}
.products-band .t{display:block;font:400 32px/34px "Roboto Condensed",sans-serif}
.tile{width:300px;height:252px}
.img-cream{background:radial-gradient(ellipse 95px 70px at 150px 150px,#fff 0%,#f4f4f4 45%,rgba(225,225,225,0) 100%),radial-gradient(ellipse 40px 18px at 130px 172px,rgba(200,60,60,.35),rgba(200,60,60,0)),linear-gradient(160deg,#f3f3f3,#dcdcdc)}
.img-tens{background:radial-gradient(ellipse 45px 85px at 150px 105px,#2a2a2c 0%,#3a3a3d 60%,rgba(58,58,61,0) 100%),radial-gradient(ellipse 90px 22px at 150px 215px,#d6d6d6,rgba(214,214,214,0)),linear-gradient(160deg,#fafafa,#ececec)}
.img-seat{background:radial-gradient(ellipse 95px 75px at 150px 120px,#1d1d1f 0%,#2b2b2e 60%,rgba(43,43,46,0) 100%),radial-gradient(ellipse 80px 22px at 160px 190px,rgba(120,130,110,.8),rgba(120,130,110,0)),linear-gradient(160deg,#f4f4f4,#e2e2e2)}
.img-brace{background:radial-gradient(ellipse 45px 55px at 165px 125px,#4d9fe0 0%,rgba(77,159,224,.5) 60%,rgba(77,159,224,0) 100%),radial-gradient(ellipse 100px 70px at 155px 125px,#24272d 0%,#30343b 60%,rgba(48,52,59,0) 100%),linear-gradient(160deg,#f4f4f4,#e4e4e4)}
.tile-text{background:var(--blue);color:var(--white);text-align:center;display:flex;flex-direction:column;align-items:center;justify-content:center}
.tile-text h3{font:400 23px "Roboto Condensed",sans-serif;text-transform:uppercase}
.tile-text p{font:400 17px "Roboto Condensed",sans-serif;margin:2px 0 22px}
.pill-btn{width:126px;height:28px;border:2px solid #a7c4de;border-radius:14px;font:400 12px "Roboto Condensed",sans-serif;display:flex;align-items:center;justify-content:center;gap:6px}
.strip{left:0;top:1785px;width:1200px;height:72px;background:repeating-linear-gradient(135deg,#fff 0 28px,#f6f6f6 28px 30px)}
.pager{top:1809px;width:26px;height:22px;background:var(--green);display:flex;align-items:center;justify-content:center}

/* features */
.panel{background:var(--grey-panel)}
.panel-title{font:700 28px "Roboto Condensed",sans-serif;color:var(--title-blue);text-transform:uppercase}
.panel-sub{display:inline-block;font:300 28px "Roboto Condensed",sans-serif;color:#444;border:2px solid #a9d99a;padding:2px 40px 2px 0;margin-top:2px}
.panel-copy{font:400 11px/18px "Open Sans",sans-serif;color:#444;margin-top:18px}
.panel-copy p+p{margin-top:8px}
.frame{border:2px solid #8fb3d3}
.photo-shoes{background:
  radial-gradient(ellipse 150px 60px at 460px 95px,rgba(140,110,90,.85),rgba(140,110,90,0)),
  radial-gradient(ellipse 170px 75px at 360px 140px,rgba(110,72,50,.9),rgba(110,72,50,0)),
  radial-gradient(ellipse 170px 85px at 230px 190px,rgba(35,35,38,.9),rgba(35,35,38,0)),
  radial-gradient(ellipse 140px 80px at 120px 250px,rgba(110,112,115,.95),rgba(110,112,115,0)),
  linear-gradient(150deg,#fafafa 0%,#f1efec 100%)}
.photo-sneaker{background:
  radial-gradient(ellipse 110px 150px at 210px 170px,rgba(140,150,170,.95),rgba(140,150,170,0)),
  radial-gradient(ellipse 110px 150px at 400px 170px,rgba(140,150,170,.95),rgba(140,150,170,0)),
  radial-gradient(ellipse 300px 60px at 300px 320px,rgba(30,25,30,.8),rgba(30,25,30,0)),
  linear-gradient(180deg,#6e3d33 0%,#5a3530 60%,#7a4050 86%,#e34fa9 100%)}
.brand-word{font:700 44px "Roboto Condensed",sans-serif;letter-spacing:1px}

/* video + catalog */
.video-title{left:162px;top:2660px;font:700 30px "Roboto Condensed",sans-serif;color:var(--title-blue);text-transform:uppercase}
.video{left:162px;top:2716px;width:504px;height:316px;border:4px solid #111;background:radial-gradient(ellipse 90px 130px at 150px 170px,#e8e8e8,rgba(232,232,232,0)),radial-gradient(ellipse 90px 130px at 340px 170px,#e8e8e8,rgba(232,232,232,0)),linear-gradient(180deg,#fdfdfd,#efefef)}
.video-bar{left:0;top:0;width:496px;height:40px;background:rgba(0,0,0,.75);color:var(--white);font:400 15px "Open Sans",sans-serif;padding:10px 12px}
.play{left:215px;top:130px;width:66px;height:48px;border-radius:12px;background:#222;display:flex;align-items:center;justify-content:center}
.catalog{left:692px;top:2656px;width:346px;height:376px;border:2px solid #a9d99a}
.catalog-head{height:54px;background:var(--green);color:var(--white);font:400 25px "Roboto Condensed",sans-serif;text-transform:uppercase;display:flex;align-items:center;justify-content:center}
.field{margin:0 32px;height:43px;border-bottom:1px solid #bbb;font:400 11px "Open Sans",sans-serif;color:#777;display:flex;align-items:flex-end;padding-bottom:6px}
.catalog-btn{left:72px;top:296px;width:200px;height:40px;background:var(--blue-dark);color:var(--white);font:400 17px "Roboto Condensed",sans-serif;text-transform:uppercase;display:flex;align-items:center;justify-content:center}

/* footer */
.badge{top:3085px;height:54px}
.footer{left:0;top:3155px;width:1200px;height:48px;background:var(--blue);color:var(--white);font:400 11px "Open Sans",sans-serif}
.footer .copy{position:absolute;left:162px;top:17px}
.social{position:absolute;top:17px;width:12px;height:12px;border-radius:50%;background:var(--white)}
</style>
</head>
<body>

<nav class="abs topnav">
  <a style="left:162px">Home</a>
  <a style="left:228px">Why Diabetic Shoes?</a>
  <a style="left:390px">Shoes</a>
  <a style="left:720px">Products</a>
  <a style="left:808px">Shoe Fitter Jobs</a>
  <a style="left:930px">FAQ</a>
  <a style="left:975px">Contact Us</a>
</nav>

<section class="abs hero" role="img" aria-label="Photo looking down at a person's legs in dark jeans and brown leather shoes on a wooden deck"></section>
<div class="abs hero-shade"></div>
<svg class="abs brand-plate" viewBox="0 0 260 128" style="z-index:3" aria-hidden="true">
  <polygon points="0,0 260,0 130,128" fill="#fff"/>
</svg>
<div class="abs brand-name" style="z-index:4">Stride Well Feet</div>
<div class="abs hero-kicker">Diabetic Shoes or Sneakers</div>
<div class="abs hero-title">Covered by Vitacor</div>
<p class="abs hero-sub">No or little out of pocket Cost To You! Vitacor, and most insurance plans, may cover the cost of one pair of diabetic shoes and three pairs of custom inserts per calendar year. Co-payments, deductibles and some restrictions apply.</p>
<div class="abs hero-btn"><svg width="14" height="14" viewBox="0 0 14 14"><circle cx="7" cy="7" r="7" fill="#fff"/><path d="M5.5 4l3 3-3 3" stroke="#4a7fad" stroke-width="1.8" fill="none"/></svg>View our Products</div>
<div class="abs hero-arrow" style="left:26px"><svg width="14" height="14" viewBox="0 0 14 14"><path d="M9 2L4 7l5 5" stroke="#fff" stroke-width="2" fill="none"/></svg></div>
<div class="abs hero-arrow" style="left:1124px"><svg width="14" height="14" viewBox="0 0 14 14"><path d="M5 2l5 5-5 5" stroke="#fff" stroke-width="2" fill="none"/></svg></div>

<section class="abs steps-band"></section>
<div class="abs steps-kicker">4 Easy Steps to Receive</div>
<h2 class="abs steps-title">Your New Therapeutic Shoes:</h2>
<div class="abs step-card" style="left:162px">
  <svg width="40" height="48" viewBox="0 0 40 48"><path d="M4 0h22l12 12v36H4z" fill="#4a7fad"/><path d="M26 0v12h12" fill="#8fb3d3"/><rect x="11" y="22" width="20" height="3" fill="#fff"/><rect x="11" y="30" width="20" height="3" fill="#fff"/><rect x="11" y="38" width="14" height="3" fill="#fff"/></svg>
  Fill out an application to see if you qualify.
</div>
<div class="abs step-card" style="left:384px">
  <svg width="46" height="46" viewBox="0 0 46 46"><circle cx="23" cy="23" r="22" fill="#4a7fad"/><path d="M14 32l2-7 13-13 5 5-13 13z" fill="#fff"/></svg>
  A prescription will be faxed to your primary physician.
</div>
<div class="abs step-card" style="left:604px">
  <svg width="76" height="46" viewBox="0 0 76 46"><path d="M4 34c0-10 2-22 8-26 6 6 16 8 24 6 8 8 22 10 34 14 4 2 4 8 2 10H4z" fill="#4a7fad"/><rect x="2" y="38" width="72" height="6" rx="3" fill="#4a7fad"/></svg>
  After the prescription is signed, a certified shoe fitter will fit your new shoes.
</div>
<div class="abs step-card" style="left:824px">
  <svg width="44" height="46" viewBox="0 0 44 46"><rect x="2" y="20" width="9" height="24" fill="#4a7fad"/><path d="M14 20l10-18c4 0 6 3 5 8l-2 8h12c4 0 5 4 3 6l-4 18H14z" fill="#4a7fad"/></svg>
  Enjoy your new shoes!
</div>

<h2 class="abs q-title">How does diabetes <span class="light">cause foot problems?</span></h2>
<p class="abs q-copy">Diabetes can cause neuropathy (nerve damage), which reduces feeling in your feet. This makes you less likely to feel the early warning signs of foot problems. Decreased circulation reduces the ability to heal and fight off infection. These two conditions significantly increase the likelihood of foot complications, infection, and ulceration.</p>
<div class="abs phone-pill">1-800-555-0147</div>

<section class="abs products-band"><span class="k">Click Here for</span><span class="t">Our Vitacor Products</span></section>
<div class="abs tile img-cream" style="left:0;top:1277px;height:256px" role="img" aria-label="Open white jar of neuropathy pain cream with a mortar and pestle"></div>
<div class="abs tile tile-text" style="left:300px;top:1277px;height:256px"><h3>Neuropathy Pain Cream</h3><p>Covered By Vitacor</p><div class="pill-btn"><svg width="10" height="10" viewBox="0 0 10 10"><circle cx="5" cy="5" r="5" fill="#fff"/><path d="M4 2.8L6.2 5 4 7.2" stroke="#4a7fad" stroke-width="1.4" fill="none"/></svg>View Details</div></div>
<div class="abs tile img-tens" style="left:600px;top:1277px;height:256px" role="img" aria-label="Black TENS unit with electrode pads"></div>
<div class="abs tile tile-text" style="left:900px;top:1277px;height:256px"><h3>TENS Unit</h3><p>Common Medical Conditions</p><div class="pill-btn"><svg width="10" height="10" viewBox="0 0 10 10"><circle cx="5" cy="5" r="5" fill="#fff"/><path d="M4 2.8L6.2 5 4 7.2" stroke="#4a7fad" stroke-width="1.4" fill="none"/></svg>View Details</div></div>
<div class="abs tile tile-text" style="left:0;top:1533px"><h3>Seat Lift</h3><p>Covered By Vitacor</p><div class="pill-btn"><svg width="10" height="10" viewBox="0 0 10 10"><circle cx="5" cy="5" r="5" fill="#fff"/><path d="M4 2.8L6.2 5 4 7.2" stroke="#4a7fad" stroke-width="1.4" fill="none"/></svg>View Details</div></div>
<div class="abs tile img-seat" style="left:300px;top:1533px" role="img" aria-label="Black portable seat lift cushion"></div>
<div class="abs tile tile-text" style="left:600px;top:1533px"><h3>Back Brace</h3><p>Covered By Vitacor</p><div class="pill-btn"><svg width="10" height="10" viewBox="0 0 10 10"><circle cx="5" cy="5" r="5" fill="#fff"/><path d="M4 2.8L6.2 5 4 7.2" stroke="#4a7fad" stroke-width="1.4" fill="none"/></svg>View Details</div></div>
<div class="abs tile img-brace" style="left:900px;top:1533px" role="img" aria-label="Black and blue lumbar back brace"></div>
<div class="abs strip"></div>
<div class="abs pager" style="left:570px"><svg width="10" height="8" viewBox="0 0 10 8"><path d="M10 4H2M4 1L1 4l3 3" stroke="#fff" stroke-width="1.5" fill="none"/></svg></div>
<div class="abs pager" style="left:606px"><svg width="10" height="8" viewBox="0 0 10 8"><path d="M0 4h8M6 1l3 3-3 3" stroke="#fff" stroke-width="1.5" fill="none"/></svg></div>

<section class="abs panel" style="left:0;top:1857px;width:594px;height:365px;padding:66px 60px 0 162px">
  <h2 class="panel-title">Why are properly fitted</h2>
  <div class="panel-sub">Shoes Important?</div>
  <div class="panel-copy">
    <p>Twenty four million people have diabetes, and twenty-five percent of this population will develop foot problems caused by their disease. We provide the most fashionable orthopedic shoes available, in a variety of styles and brands, to help treat and prevent painful diabetic symptoms.</p>
    <p>Our orthopedic shoes reduce the pressure and friction on your feet that can lead to foot injuries. Custom inserts relieve pressure and cushion your feet. Diabetic Socks and our therapeutic shoes are also accurately sized and padded to ensure that there is enough room in the toe-box, heel, and arch of the shoe. All of these features provide you with the very best in comfort and help prevent potential foot complications.</p>
  </div>
</section>
<div class="abs frame photo-shoes" style="left:602px;top:1866px;width:580px;height:356px" role="img" aria-label="Group of grey, black and brown orthopedic shoes with straps and laces"></div>
<div class="abs brand-word" style="left:962px;top:2160px;color:#222">PEDORA</div>

<div class="abs photo-sneaker" style="left:0;top:2233px;width:594px;height:376px" role="img" aria-label="Feet in grey and orange knit sneakers on a wooden deck"></div>
<div class="abs" style="left:12px;top:2243px;width:572px;height:356px;border:2px solid rgba(255,255,255,.8)"></div>
<div class="abs brand-word" style="left:16px;top:2400px;color:#fff">PEDORA</div>
<section class="abs panel" style="left:602px;top:2233px;width:598px;height:376px;padding:66px 110px 0 14px">
  <h2 class="panel-title">How do you know if</h2>
  <div class="panel-sub">Orthopedic Shoes Are Right For You?</div>
  <div class="panel-copy"><p>Anyone with Diabetic Neuropathy, poor circulation, high risk of infection or nerve damage can benefit from diabetic socks and our shoes. Vitacor patients who qualify are eligible for one pair of shoes and three sets of custom insoles per year – at no out of pocket cost to them. Additionally, most private insurance companies will cover the same benefits as Vitacor.</p></div>
</section>

<h2 class="abs video-title">Diabetic Shoes Video:</h2>
<div class="abs video" role="img" aria-label="Video still: line drawing of a shoe fitter measuring a seated man's foot">
  <div class="abs video-bar">How to get diabetic shoes from Vitacor at no cost to you?</div>
  <div class="abs play"><svg width="22" height="24" viewBox="0 0 22 24"><path d="M0 0l22 12L0 24z" fill="#fff"/></svg></div>
</div>

<form class="abs catalog">
  <div class="catalog-head">Request a Free Catalog</div>
  <div class="field">Name*</div>
  <div class="field">Company Name*</div>
  <div class="field">Email ID*</div>
  <div class="field">Mobile Number*</div>
  <div class="field" style="height:50px">Query*</div>
  <div class="abs catalog-btn">Request Catalog</div>
</form>

<div class="abs badge" style="left:532px;width:40px;background:#1f6b4f" role="img" aria-label="Accreditation badge"></div>
<div class="abs badge" style="left:604px;top:3098px;width:66px;height:30px;background:#222" role="img" aria-label="Compliance badge"></div>

<footer class="abs footer">
  <span class="copy">© Copyright Stride Well Feet - All Rights Reserved</span>
  <span class="social" style="left:950px"></span>
  <span class="social" style="left:970px"></span>
  <span class="social" style="left:990px"></span>
  <span class="social" style="left:1010px"></span>
</footer>

</body>
</html>
```